Marova Hand Wash

Design hand washes. Total 12 variants to be designed.

Variants name are:

1) MILK &OLIVE
2) Shea Butter
3) Hidden Glow
4) Cream and Peach
5) Milk and Honey
6) Amber Riddle
7) Bakhour
8) Musk
9) White Oud
10) Black Oud
11) Rose Oud
12) Oud & Sandalwood

Labels can be on transparent sticker or background colors. All variants will be differentiated by fragrances and color. Bottle will be transparent. Pumps used for dispensing will be in Black or Transparent Color.

Designers can initially present designs of 4-5 variants initially. Later based on feedback, they can work out on more.

Bottle is 400ml and shape is rectangle. Ignore the size on bottle picture. Bottle keyline is attached.

Target Market(s)

B+, B, C+

Requirements
Must have
• Some relation to the variant names

```html
<!DOCTYPE html>
<html lang="en">
<head>
<meta charset="utf-8">
<title>Marova Hand Wash Range</title>
<link href="https://fonts.googleapis.com/css2?family=Lato:wght@400;700&family=Kaushan+Script&display=swap" rel="stylesheet">
<style>
  :root {
    --page: #ffffff;
    --brand: #5a4a9c;
    --pump-light: #f4f4f4;
    --pump-dark: #c9c9c9;
    --label-text: #4a4a4a;
  }
  html, body { margin: 0; padding: 0; overflow: hidden; }
  body { width: 770px; height: 1200px; background: var(--page); font-family: 'Lato', sans-serif; }
  .range {
    position: relative; width: 770px; height: 1200px;
    display: grid; grid-template-columns: repeat(4, 136px); grid-auto-rows: 320px;
    column-gap: 27px; row-gap: 54px; padding: 64px 0 0 72px; box-sizing: border-box;
  }
  .bottle { position: relative; width: 136px; height: 320px; }
  .pump { position: absolute; top: 0; left: 0; width: 136px; height: 92px; }
  .body {
    position: absolute; top: 90px; left: 0; width: 136px; height: 230px;
    border-radius: 16px; background: linear-gradient(90deg, var(--tint-dark), var(--tint) 20%, var(--tint) 80%, var(--tint-dark));
    box-shadow: 0 10px 12px -8px rgba(0,0,0,0.15);
  }
  .label {
    position: absolute; top: 14px; left: 17px; right: 17px; bottom: 22px; border-radius: 6px;
    background: linear-gradient(180deg, #ffffff 0%, #fbfbfb 45%, var(--wash) 100%);
    text-align: center; overflow: hidden;
  }
  .brand-name { margin-top: 14px; font-size: 19px; font-weight: 400; color: var(--brand); letter-spacing: 0.2px; line-height: 1; }
  .brand-rule { width: 60px; height: 1px; margin: 5px auto 0; background: #8cbf3f; }
  .note { margin-top: 10px; font-size: 10px; color: var(--note, var(--label-text)); line-height: 1; }
  .note.empty { visibility: hidden; }
  .scent { font-family: 'Kaushan Script', cursive; font-size: 22px; color: var(--accent); line-height: 1.1; margin-top: 1px; }
  .art { position: absolute; left: 50%; bottom: 38px; width: 62px; height: 40px; transform: translateX(-50%); border-radius: 14px; background: radial-gradient(circle at 50% 55%, var(--art1), var(--art2) 70%, transparent 100%); }
  .tag {
    position: absolute; left: 50%; bottom: 0; width: 36px; height: 44px; transform: translateX(-50%);
    background: var(--box); color: #ffffff; font-size: 5.5px; letter-spacing: 1.2px; line-height: 1.25;
    display: flex; flex-direction: column; align-items: center; justify-content: center;
  }
  .tag .vol { margin-top: 4px; font-size: 4.5px; letter-spacing: 0.3px; border-top: 1px solid rgba(255,255,255,0.6); padding-top: 3px; }

  .olive   { --tint:#c5d67a; --tint-dark:#a9bf58; --wash:#e5f0c4; --accent:#35661f; --box:#2f5a1d; --art1:#9bbf3c; --art2:#5e8a24; }
  .peach   { --tint:#f9a97c; --tint-dark:#ef9060; --wash:#fde1d0; --accent:#8c2d20; --box:#8a2d1f; --art1:#f6a23a; --art2:#e0582b; }
  .amber   { --tint:#f3ecdd; --tint-dark:#e2d7c0; --wash:#efe3cc; --accent:#8b6a47; --box:#9c7a52; --art1:#f5f0e4; --art2:#6b4a2c; --note:#8b6a47; }
  .rose    { --tint:#db839c; --tint-dark:#c96b86; --wash:#f6d4de; --accent:#c4185a; --box:#c4185a; --art1:#f4a3b6; --art2:#3e7d3a; }
  .sandal  { --tint:#f7951e; --tint-dark:#e27f0c; --wash:#f0d6c4; --accent:#3b1a10; --box:#4d2317; --art1:#b4593a; --art2:#5c2b1b; }
  .musk    { --tint:#f26b36; --tint-dark:#dc5424; --wash:#fbd3c3; --accent:#a3262a; --box:#a3262a; --art1:#c4b58a; --art2:#6b5a36; }
  .honey   { --tint:#d97b2b; --tint-dark:#c2661c; --wash:#fbe1b9; --accent:#e0811c; --box:#e08a1e; --art1:#f7c04a; --art2:#d7781a; --note:#e08a1e; }
  .shea    { --tint:#f2e7c2; --tint-dark:#e2d3a2; --wash:#eee5c8; --accent:#3c3b2c; --box:#5a5a4e; --art1:#f1ede3; --art2:#6b4a2a; }
  .glow    { --tint:#1f61a3; --tint-dark:#17508a; --wash:#d4e2f2; --accent:#1b4d8f; --box:#1c4e8f; --art1:#f3b23a; --art2:#2d7a3a; --note:#1b4d8f; }
  .bakhour { --tint:#d9263b; --tint-dark:#bd1b2e; --wash:#f8d0d4; --accent:#a31c2b; --box:#a51c2b; --art1:#b8894a; --art2:#5b3a1a; }
  .whiteoud{ --tint:#f4f0e4; --tint-dark:#e4dece; --wash:#f3ead2; --accent:#d4a13f; --box:#d6a850; --art1:#b58a5a; --art2:#5e4027; --note:#d4a13f; }
  .blackoud{ --tint:#575757; --tint-dark:#3e3e3e; --wash:#d4d4d4; --accent:#1a1a1a; --box:#1f1f1f; --art1:#7a5a3a; --art2:#2e2116; }
</style>
</head>
<body>
<svg width="0" height="0" style="position:absolute">
  <defs>
    <linearGradient id="pump-shade" x1="0" x2="1" y1="0" y2="0">
      <stop offset="0" stop-color="#cfcfcf"/><stop offset="0.45" stop-color="#f7f7f7"/><stop offset="1" stop-color="#bdbdbd"/>
    </linearGradient>
    <symbol id="pump" viewBox="0 0 136 92">
      <path d="M30 4 Q30 0 36 0 H132 Q136 1 134 6 L128 8 H30 Z" fill="#dcdcdc"/>
      <rect x="56" y="8" width="24" height="22" fill="url(#pump-shade)"/>
      <rect x="52" y="26" width="32" height="6" rx="2" fill="#d6d6d6"/>
      <rect x="34" y="32" width="68" height="60" rx="3" fill="url(#pump-shade)"/>
    </symbol>
  </defs>
</svg>

<main class="range">
  <article class="bottle olive">
    <svg class="pump" viewBox="0 0 136 92"><use href="#pump"/></svg>
    <div class="body"><div class="label">
      <div class="brand-name">Marova</div><div class="brand-rule"></div>
      <div class="note">Milk and</div><div class="scent">Olive</div>
      <div class="art" role="img" aria-label="Green olives with leaves"></div>
      <div class="tag"><span>HAND</span><span>WASH</span><span class="vol">- 400 mL -</span></div>
    </div></div>
  </article>

  <article class="bottle peach">
    <svg class="pump" viewBox="0 0 136 92"><use href="#pump"/></svg>
    <div class="body"><div class="label">
      <div class="brand-name">Marova</div><div class="brand-rule"></div>
      <div class="note">Cream and</div><div class="scent">Peach</div>
      <div class="art" role="img" aria-label="Ripe peaches"></div>
      <div class="tag"><span>HAND</span><span>WASH</span><span class="vol">- 400 mL -</span></div>
    </div></div>
  </article>

  <article class="bottle amber">
    <svg class="pump" viewBox="0 0 136 92"><use href="#pump"/></svg>
    <div class="body"><div class="label">
      <div class="brand-name">Marova</div><div class="brand-rule"></div>
      <div class="note">Amber</div><div class="scent">Riddle</div>
      <div class="art" role="img" aria-label="Vanilla pods and white flower"></div>
      <div class="tag"><span>HAND</span><span>WASH</span><span class="vol">- 400 mL -</span></div>
    </div></div>
  </article>

  <article class="bottle rose">
    <svg class="pump" viewBox="0 0 136 92"><use href="#pump"/></svg>
    <div class="body"><div class="label">
      <div class="brand-name">Marova</div><div class="brand-rule"></div>
      <div class="note">Rose</div><div class="scent">Oud</div>
      <div class="art" role="img" aria-label="Pink rose with leaves"></div>
      <div class="tag"><span>HAND</span><span>WASH</span><span class="vol">- 400 mL -</span></div>
    </div></div>
  </article>

  <article class="bottle sandal">
    <svg class="pump" viewBox="0 0 136 92"><use href="#pump"/></svg>
    <div class="body"><div class="label">
      <div class="brand-name">Marova</div><div class="brand-rule"></div>
      <div class="note">Oud and</div><div class="scent" style="font-size:17px">Sandalwood</div>
      <div class="art" role="img" aria-label="Sandalwood pieces with green leaves"></div>
      <div class="tag"><span>HAND</span><span>WASH</span><span class="vol">- 400 mL -</span></div>
    </div></div>
  </article>

  <article class="bottle musk">
    <svg class="pump" viewBox="0 0 136 92"><use href="#pump"/></svg>
    <div class="body"><div class="label">
      <div class="brand-name">Marova</div><div class="brand-rule"></div>
      <div class="note empty">&nbsp;</div><div class="scent">Musk</div>
      <div class="art" role="img" aria-label="Dried musk roots"></div>
      <div class="tag"><span>HAND</span><span>WASH</span><span class="vol">- 400 mL -</span></div>
    </div></div>
  </article>

  <article class="bottle honey">
    <svg class="pump" viewBox="0 0 136 92"><use href="#pump"/></svg>
    <div class="body"><div class="label">
      <div class="brand-name">Marova</div><div class="brand-rule"></div>
      <div class="note">Milk and</div><div class="scent">Honey</div>
      <div class="art" role="img" aria-label="Honey dipper with splashing honey"></div>
      <div class="tag"><span>HAND</span><span>WASH</span><span class="vol">- 400 mL -</span></div>
    </div></div>
  </article>

  <article class="bottle shea">
    <svg class="pump" viewBox="0 0 136 92"><use href="#pump"/></svg>
    <div class="body"><div class="label">
      <div class="brand-name">Marova</div><div class="brand-rule"></div>
      <div class="note">Butter</div><div class="scent">Shea</div>
      <div class="art" role="img" aria-label="Shea nuts with butter and leaves"></div>
      <div class="tag"><span>HAND</span><span>WASH</span><span class="vol">- 400 mL -</span></div>
    </div></div>
  </article>

  <article class="bottle glow">
    <svg class="pump" viewBox="0 0 136 92"><use href="#pump"/></svg>
    <div class="body"><div class="label">
      <div class="brand-name">Marova</div><div class="brand-rule"></div>
      <div class="note">Hidden</div><div class="scent">Glow</div>
      <div class="art" role="img" aria-label="Tropical flowers with butterflies"></div>
      <div class="tag"><span>HAND</span><span>WASH</span><span class="vol">- 400 mL -</span></div>
    </div></div>
  </article>

  <article class="bottle bakhour">
    <svg class="pump" viewBox="0 0 136 92"><use href="#pump"/></svg>
    <div class="body"><div class="label">
      <div class="brand-name">Marova</div><div class="brand-rule"></div>
      <div class="note empty">&nbsp;</div><div class="scent">Bakhour</div>
      <div class="art" role="img" aria-label="Brass incense burner"></div>
      <div class="tag"><span>HAND</span><span>WASH</span><span class="vol">- 400 mL -</span></div>
    </div></div>
  </article>

  <article class="bottle whiteoud">
    <svg class="pump" viewBox="0 0 136 92"><use href="#pump"/></svg>
    <div class="body"><div class="label">
      <div class="brand-name">Marova</div><div class="brand-rule"></div>
      <div class="note">White</div><div class="scent">Oud</div>
      <div class="art" role="img" aria-label="Oud wood chips"></div>
      <div class="tag"><span>HAND</span><span>WASH</span><span class="vol">- 400 mL -</span></div>
    </div></div>
  </article>

  <article class="bottle blackoud">
    <svg class="pump" viewBox="0 0 136 92"><use href="#pump"/></svg>
    <div class="body"><div class="label">
      <div class="brand-name">Marova</div><div class="brand-rule"></div>
      <div class="note">Black</div><div class="scent">Oud</div>
      <div class="art" role="img" aria-label="Wooden bowl of dark oud chips"></div>
      <div class="tag"><span>HAND</span><span>WASH</span><span class="vol">- 400 mL -</span></div>
    </div></div>
  </article>
</main>
</body>
</html>
```